Redesign responsive website and logo for webshop platform

Redesign our applications old website with a new clean, crisp modern looking style that is responsive.

Our application is a cloud based, free ecommerce platform that lets users set up their own webshops within minutes. (Similar to Mabrook https://mabrook.example/l/sell)

Our old website: http://sv.vendlyx.example/

I need redesigned HTML + CSS for the following three pages:
* Landing Page:
(Old page: http://sv.vendlyx.example/)
I have attached a mockup of a proposed layout/structure for the landing page.
- Pricing comparision/features page
(Old page http://sv.vendlyx.example/t/funktioner)
- Generic "article" page:
(Old page http://sv.vendlyx.example/d/redigerasida)

The pages must responsive using HTML 5/CSS 3 (I prefer Bootstrap 3 if possible).

I also need a redesign of the logotype.

If you have any questions don't hesitate to ask and we will provide whatever is needed to you.

Logo Text

Vendlyx

Coding

Coded - Design and coding required

Number of Pages Required

3 page

Font styles to use
Serif
Sans Serif

```html
<!DOCTYPE html>
<html lang="sv">
<head>
<meta charset="utf-8">
<title>Vendlyx – Funktioner</title>
<link href="https://fonts.googleapis.com/css2?family=Questrial&display=swap" rel="stylesheet">
<style>
:root{
  --page:#f2f2f2;
  --cell:#f6f6f6;
  --section:#ececec;
  --line:#ffffff;
  --blue:#2a9fd8;
  --blue-dark:#1f5fae;
  --text:#333;
  --muted:#666;
  --white:#fff;
}
*{box-sizing:border-box;margin:0;padding:0}
html,body{width:712px;height:1200px;overflow:hidden}
body{background:var(--page);font-family:"Questrial",sans-serif;color:var(--text);position:relative}
.site-header{position:absolute;top:0;left:0;width:712px;height:40px;background:var(--white);box-shadow:0 1px 3px rgba(0,0,0,.2)}
.contact{position:absolute;top:16px;font-size:6.2px;color:var(--muted);display:flex;align-items:center;gap:4px;white-space:nowrap}
.contact i{width:5px;height:5px;background:var(--blue);display:inline-block}
.contact.mail{left:102px}.contact.social{left:190px}
.brand{position:absolute;left:300px;top:11px;display:flex;align-items:center;gap:6px;font-size:16px;font-weight:400;color:var(--blue);letter-spacing:1px}
.brand i{width:12px;height:12px;border-radius:50%;background:var(--blue);display:inline-block}
.auth{position:absolute;top:13px;right:104px;display:flex;gap:6px}
.auth a{background:var(--blue);color:var(--white);font-size:6.5px;text-decoration:none;padding:4px 6px;box-shadow:1px 1px 0 #1d7fb0}
.features{position:absolute;left:102px;top:60px;width:428px}
.features h1{font-weight:400;font-size:11.5px;color:var(--blue-dark);margin-bottom:5px}
.features p{font-size:5.4px;color:var(--muted);line-height:1.3;margin-bottom:6px}
.plans{border-collapse:collapse;width:428px;table-layout:fixed;margin-top:18px}
.plans td,.plans th{height:17.6px;border-bottom:1px solid var(--line);font-size:7.5px;text-align:center;font-weight:400;color:var(--blue)}
.plans td+td,.plans th+th{border-left:1px solid var(--line)}
.plans td{background:var(--cell)}
.plans th{background:var(--section);color:var(--text);font-size:7.8px}
.plans .group td{background:var(--section);color:var(--text);font-size:7.8px}
.plans col.name{width:244px}.plans col.plan{width:92px}
.tick{width:13px;height:12px;vertical-align:middle}
.footnote{position:absolute;left:152px;top:974px;font-size:5.6px;color:var(--muted)}
.cta{position:absolute;left:0;top:999px;width:712px;height:201px;background:linear-gradient(100deg,#1e5eb1 0%,#2164b5 55%,#3a78bd 100%)}
.cta-visual{position:absolute;left:392px;top:8px;width:320px;height:168px;background:linear-gradient(135deg,rgba(190,210,235,.55),rgba(90,140,200,.35) 60%,rgba(60,110,180,.2));}
.cta h2{position:absolute;left:102px;top:12px;font-weight:400;font-size:14px;color:var(--white)}
.tabs{position:absolute;left:102px;top:33px;display:flex;gap:5px}
.tabs span{border:1px solid rgba(255,255,255,.8);color:var(--white);font-size:7px;padding:2px 6px}
.tabs .active{background:var(--blue)}
.field{position:absolute;font-size:5.6px;color:var(--white);border-bottom:1px solid rgba(255,255,255,.35);padding-bottom:6px}
.f1{left:102px;top:53px;width:260px}
.f2{left:102px;top:72px;width:280px;height:24px}
.f3{left:102px;top:103px;width:110px}
.f4{left:240px;top:103px;width:130px}
.send{position:absolute;left:102px;top:128px;width:51px;height:19px;background:var(--blue);color:var(--white);font-size:8px;display:flex;align-items:center;justify-content:center}
.copyright{position:absolute;left:102px;top:171px;width:508px;border-top:1px solid rgba(255,255,255,.4);text-align:center;font-size:5.8px;color:var(--white);padding-top:6px}
</style>
</head>
<body>
<svg width="0" height="0" style="position:absolute">
  <symbol id="tick" viewBox="0 0 13 12"><path d="M0.5 6.5 L3 4.5 L5 7 L11 0.5 L12.5 2 L5 11 Z" fill="#2a9fd8"/></symbol>
</svg>

<header class="site-header">
  <span class="contact mail"><i></i>info@vendlyx.example</span>
  <span class="contact social"><i></i>Vendlyx på Chirper</span>
  <div class="brand"><i></i>VENDLYX</div>
  <nav class="auth"><a href="#">SIGN IN</a><a href="#">LOG IN</a></nav>
</header>

<main class="features">
  <h1>Funktioner</h1>
  <p>Följande är några av Vendlyx nyckelfunktioner. Tabellen nedan visar vilka av funktionerna som är tillgängliga för respektive kontotyper.</p>
  <p>Du som startat med gratisversionen kommer inom kort kunna uppgradera till premiumversionen för att få mer funktionalitet.</p>
  <table class="plans">
    <colgroup><col class="name"><col class="plan"><col class="plan"></colgroup>
    <tr><th>Funktioner</th><th>Standardkonto</th><th>Premiumkonto</th></tr>
    <tr><td>Kostnad</td><td>Gratis</td><td>Från 149kr/mån</td></tr>
    <tr><td>Transaktionsavgift</td><td>0%</td><td>0%</td></tr>
    <tr class="group"><td>Tekniska specifikationer</td><td></td><td></td></tr>
    <tr><td>Obegränsat antal produkter</td><td><svg class="tick"><use href="#tick"/></svg></td><td><svg class="tick"><use href="#tick"/></svg></td></tr>
    <tr><td>Obegränsad datatrafik</td><td><svg class="tick"><use href="#tick"/></svg></td><td><svg class="tick"><use href="#tick"/></svg></td></tr>
    <tr><td>Antal bilder/utrymme</td><td>Obegränsat</td><td>Obegränsat</td></tr>
    <tr><td>Enkel webshop design</td><td><svg class="tick"><use href="#tick"/></svg></td><td><svg class="tick"><use href="#tick"/></svg></td></tr>
    <tr><td>Lagerhantering</td><td><svg class="tick"><use href="#tick"/></svg></td><td><svg class="tick"><use href="#tick"/></svg></td></tr>
    <tr><td>Sökmotoroptimerad (SEO)</td><td><svg class="tick"><use href="#tick"/></svg></td><td><svg class="tick"><use href="#tick"/></svg></td></tr>
    <tr><td>Skapa egna betalsätt</td><td><svg class="tick"><use href="#tick"/></svg></td><td><svg class="tick"><use href="#tick"/></svg></td></tr>
    <tr><td>Kortbetalning med Paynord</td><td><svg class="tick"><use href="#tick"/></svg></td><td><svg class="tick"><use href="#tick"/></svg></td></tr>
    <tr><td>Fakturo Faktura betalning</td><td><svg class="tick"><use href="#tick"/></svg></td><td><svg class="tick"><use href="#tick"/></svg></td></tr>
    <tr><td>Redigera frakttyper</td><td><svg class="tick"><use href="#tick"/></svg></td><td><svg class="tick"><use href="#tick"/></svg></td></tr>
    <tr><td>Olika fraktpriser beroende på ordervikt</td><td><svg class="tick"><use href="#tick"/></svg></td><td><svg class="tick"><use href="#tick"/></svg></td></tr>
    <tr><td>Snabbkassa</td><td></td><td><svg class="tick"><use href="#tick"/></svg></td></tr>
    <tr><td>Favicon stöd</td><td><svg class="tick"><use href="#tick"/></svg></td><td><svg class="tick"><use href="#tick"/></svg></td></tr>
    <tr><td>Hantera leverantörer</td><td><svg class="tick"><use href="#tick"/></svg></td><td><svg class="tick"><use href="#tick"/></svg></td></tr>
    <tr><td>Smart Dashboard</td><td><svg class="tick"><use href="#tick"/></svg></td><td><svg class="tick"><use href="#tick"/></svg></td></tr>
    <tr><td>Vänbok-kommentarer</td><td><svg class="tick"><use href="#tick"/></svg></td><td><svg class="tick"><use href="#tick"/></svg></td></tr>
    <tr><td>Vänbok like box</td><td></td><td><svg class="tick"><use href="#tick"/></svg></td></tr>
    <tr><td>Vänbok shop</td><td></td><td><svg class="tick"><use href="#tick"/></svg></td></tr>
    <tr><td>Stöder Vänbok Open Graph Protocol</td><td><svg class="tick"><use href="#tick"/></svg></td><td><svg class="tick"><use href="#tick"/></svg></td></tr>
    <tr><td>WebbNorm Standardiserad HTML-kod</td><td><svg class="tick"><use href="#tick"/></svg></td><td><svg class="tick"><use href="#tick"/></svg></td></tr>
    <tr><td>Bildspel</td><td><svg class="tick"><use href="#tick"/></svg></td><td><svg class="tick"><use href="#tick"/></svg></td></tr>
    <tr><td>Produktvarianter</td><td><svg class="tick"><use href="#tick"/></svg></td><td><svg class="tick"><use href="#tick"/></svg></td></tr>
    <tr><td>Avancerade produktvarianter</td><td></td><td><svg class="tick"><use href="#tick"/></svg></td></tr>
    <tr><td>Eget HTML-innehåll</td><td></td><td><svg class="tick"><use href="#tick"/></svg></td></tr>
    <tr><td>Framhävda produkter i högerkolumn</td><td></td><td><svg class="tick"><use href="#tick"/></svg></td></tr>
    <tr><td>Flera administratörer</td><td></td><td><svg class="tick"><use href="#tick"/></svg></td></tr>
    <tr class="group"><td>Kunder och affärer</td><td></td><td></td></tr>
    <tr><td>Kundregister</td><td><svg class="tick"><use href="#tick"/></svg></td><td><svg class="tick"><use href="#tick"/></svg></td></tr>
    <tr><td>Orderhantering</td><td><svg class="tick"><use href="#tick"/></svg></td><td><svg class="tick"><use href="#tick"/></svg></td></tr>
    <tr><td>Avancerad orderhantering</td><td></td><td><svg class="tick"><use href="#tick"/></svg></td></tr>
    <tr><td>Automatiska ordermail</td><td></td><td><svg class="tick"><use href="#tick"/></svg></td></tr>
    <tr><td>Inbyggt analysverktyg</td><td><svg class="tick"><use href="#tick"/></svg></td><td><svg class="tick"><use href="#tick"/></svg></td></tr>
    <tr><td>Automatgenererade Sitemaps</td><td><svg class="tick"><use href="#tick"/></svg></td><td><svg class="tick"><use href="#tick"/></svg></td></tr>
    <tr><td>Epostnotifieringar vid inkomna ordrar</td><td><svg class="tick"><use href="#tick"/></svg></td><td><svg class="tick"><use href="#tick"/></svg></td></tr>
    <tr class="group"><td>Marknadsföring</td><td></td><td></td></tr>
    <tr><td>Social delningsfunktion</td><td><svg class="tick"><use href="#tick"/></svg></td><td><svg class="tick"><use href="#tick"/></svg></td></tr>
    <tr><td>Lägg in produkter på bloggar/hemsidor</td><td><svg class="tick"><use href="#tick"/></svg></td><td><svg class="tick"><use href="#tick"/></svg></td></tr>
    <tr><td>Integration till Prisvakt</td><td><svg class="tick"><use href="#tick"/></svg></td><td><svg class="tick"><use href="#tick"/></svg></td></tr>
    <tr><td>Rabattkoder</td><td></td><td><svg class="tick"><use href="#tick"/></svg></td></tr>
    <tr class="group"><td>Övrigt</td><td></td><td></td></tr>
    <tr><td>Egen domän</td><td></td><td><svg class="tick"><use href="#tick"/></svg></td></tr>
    <tr><td>E-postsupport</td><td><svg class="tick"><use href="#tick"/></svg></td><td><svg class="tick"><use href="#tick"/></svg></td></tr>
    <tr><td>Integration till Prisvakt</td><td></td><td><svg class="tick"><use href="#tick"/></svg></td></tr>
    <tr><td>Sökly Ads kupong (värde 750kr) *</td><td></td><td><svg class="tick"><use href="#tick"/></svg></td></tr>
  </table>
</main>
<p class="footnote">* Kupongerna är endast till för nya Sökly Ads-kunder</p>

<footer class="cta">
  <div class="cta-visual" role="img" aria-label="Bärbar dator på ett kafébord som visar Vendlyx startsida"></div>
  <h2>Discover Vendlyx. Start Your Shop Today.</h2>
  <div class="tabs"><span class="active">Frågor</span><span>Förslag</span><span>Problem</span><span>Beröm</span></div>
  <div class="field f1">Beskriv Kortfattat Din Fråga</div>
  <div class="field f2">Ge En Längre Beskrivning Av Ärendet</div>
  <div class="field f3">Din e-Post</div>
  <div class="field f4">Ditt Namn</div>
  <div class="send">SKICKA</div>
  <div class="copyright">© 2016 Nordkod | Support | Dokumentation</div>
</footer>
</body>
</html>
```